Permanent Holiday Lights - Yard Sign

This project aims to create a visually compelling yard sign that proudly represents the GlowCrest brand and draws attention in residential neighborhoods. The sign will serve as both a marketing tool and a badge of pride for customers who have chosen GlowCrest’ permanent lighting solutions. The design should capture GlowCrest’ premium, modern aesthetic while ensuring high visibility and readability from a distance.
Objectives:
Increase brand visibility in neighborhoods with GlowCrest installations.
Reinforce brand identity through consistent use of GlowCrest colors, logo, and typography.
Inspire curiosity and engagement, prompting passersby to visit the website or contact GlowCrest for more information.
Design Goals:
Use GlowCrest brand colors to ensure brand consistency and recognition.
Feature the GlowCrest logo prominently.
Include a clear, easy-to-read message — e.g.,

Does not require use of a home but am attaching pictures that could be used if the designer likes that.

Emphasize contrast and legibility, even at a distance or in various lighting conditions.
Incorporate a clean, modern design that reflects innovation and premium quality.
Deliverables:
Primary yard sign design (36”x24”, landscape orientation preferred)
Optional alternate versions for seasonal or promotional use
Print-ready files (CMYK, high-resolution PDF)
Digital mockups for presentation
Target Audience:
Homeowners and neighbors who value aesthetics, technology, and convenience—potential customers curious about GlowCrest when they see them in action.
Tone & Style:
Bright, confident, and contemporary
Reflects innovation, reliability, and lasting beauty
Clean and professional

Potential Tag Lines:
“We just added 4 billion colors to our home. Ask me about my new GlowCrest.”
“Our GlowCrest stays up. Our ladder stays down.”
“GlowCrest did this. (Arrow up) Come back at night to see what ‘this’ is.”

On the sign, please include either the website URL: www.mynovaglowhome.example OR the phone number: 555.418.7360

Target Market(s)

Middle to upper class (can be retired or have families) - interested in decor, having the nicest home in the block, and home improvements

Industry/Entity Type

Permanent Christmas Lights

Requirements
Must have
• On the sign, please include either the website URL: www.mynovaglowhome.example OR the phone number: 555.418.7360, A slogan /tag line like the ones I shared in the description. Captivating and colorful design.

```html
<!DOCTYPE html>
<html lang="en">
<head>
<meta charset="utf-8">
<title>GlowCrest Yard Sign</title>
<link rel="stylesheet" href="https://fonts.googleapis.com/css2?family=Montserrat:wght@400;500;700&display=swap">
<style>
  :root {
    --page-light: #f4f4f4;
    --page-dark: #a9a9a9;
    --sign-black: #000000;
    --white: #ffffff;
    --tag-yellow: #f6c21c;
    --tag-orange: #f2962b;
    --pill-gold: #c9a23c;
    --glow-navy: rgba(22, 40, 110, 0.55);
    --glow-olive: rgba(120, 95, 10, 0.5);
    --glow-green: rgba(20, 90, 20, 0.55);
    --glow-red: rgba(120, 20, 20, 0.45);
    --glow-rust: rgba(110, 50, 10, 0.45);
    --spectrum: conic-gradient(from 0deg,
      #e23b8f 0deg, #9a4fb4 30deg, #4fc49a 55deg, #3f6fd0 75deg,
      #5b8fd6 95deg, #7a55b8 125deg, #b04aa8 150deg, #e8397a 175deg,
      #e52f3a 195deg, #f7882a 215deg, #f4c51c 235deg, #8cc63f 255deg,
      #7cc242 270deg, #f6b81f 295deg, #f48a2a 320deg, #ee3d3d 345deg, #e23b8f 360deg);
  }
  * { box-sizing: border-box; margin: 0; padding: 0; }
  html, body { width: 847px; height: 1200px; overflow: hidden; }
  body {
    background: radial-gradient(ellipse at 35% 40%, var(--page-light) 0%, #d6d6d6 60%, var(--page-dark) 100%);
    font-family: "Montserrat", sans-serif;
    position: relative;
  }
  .yard-sign {
    position: absolute;
    left: 44px;
    top: 346px;
    width: 760px;
    height: 507px;
    background: var(--spectrum);
    padding: 19px;
    box-shadow: -14px 16px 26px rgba(0, 0, 0, 0.35);
  }
  .sign-face {
    position: relative;
    width: 100%;
    height: 100%;
    background: var(--sign-black);
    color: var(--white);
    text-align: center;
    overflow: hidden;
  }
  .ambient-glow {
    position: absolute;
    inset: 0;
    background:
      radial-gradient(ellipse 190px 120px at 150px 60px, var(--glow-navy), transparent 75%),
      radial-gradient(ellipse 190px 120px at 580px 70px, var(--glow-olive), transparent 75%),
      radial-gradient(ellipse 80px 110px at 361px 70px, var(--glow-green), transparent 80%),
      radial-gradient(ellipse 60px 50px at 120px 250px, var(--glow-green), transparent 80%),
      radial-gradient(ellipse 120px 60px at 620px 310px, var(--glow-rust), transparent 80%),
      radial-gradient(ellipse 140px 50px at 470px 470px, var(--glow-red), transparent 80%),
      radial-gradient(ellipse 110px 45px at 240px 470px, var(--glow-navy), transparent 80%);
  }
  .brand-circle {
    position: absolute;
    left: 50%;
    top: 48px;
    width: 96px;
    height: 96px;
    transform: translateX(-50%);
    border-radius: 50%;
    background: var(--tag-yellow);
  }
  .brand-name {
    position: absolute;
    left: 0; right: 0;
    top: 188px;
    font-weight: 500;
    font-size: 42px;
    letter-spacing: 10px;
    line-height: 1;
    color: var(--white);
  }
  .tagline {
    position: absolute;
    left: 0; right: 0;
    top: 252px;
    font-weight: 400;
    font-size: 44px;
    line-height: 58px;
  }
  .tagline-first { color: var(--tag-yellow); display: block; }
  .tagline-second { color: var(--tag-orange); display: block; }
  .tagline-brand { color: var(--white); font-weight: 700; }
  .web-address {
    position: absolute;
    left: 50%;
    top: 398px;
    transform: translateX(-50%);
    width: 456px;
    height: 40px;
    border: 1.5px solid var(--pill-gold);
    border-radius: 20px;
    display: flex;
    align-items: center;
    justify-content: center;
    font-size: 16px;
    letter-spacing: 3px;
    color: var(--white);
    white-space: nowrap;
  }
</style>
</head>
<body>
  <div class="yard-sign">
    <div class="sign-face">
      <div class="ambient-glow" role="img" aria-label="Faint coloured light rays glowing across the dark sign background"></div>
      <span class="brand-circle"></span>
      <div class="brand-name">GLOWCREST</div>
      <p class="tagline">
        <span class="tagline-first">Our <span class="tagline-brand">GLOWCREST</span> stays up.</span>
        <span class="tagline-second">Our ladder stays down.</span>
      </p>
      <div class="web-address">WWW.MYNOVAGLOWHOME.EXAMPLE</div>
    </div>
  </div>
</body>
</html>
```